Business Card Design for Quillmoreton Carpentry

I need a business card design for my carpentry company Quillmoreton Carpentry. Ive attached files with all information I require on both sides. Look forward to seeing your design.

```html
<!DOCTYPE html>
<html lang="en">
<head>
<meta charset="utf-8">
<title>Quillmoreton Carpentry – Business Card</title>
<link href="https://fonts.googleapis.com/css2?family=Oswald:wght@400&family=Roboto:wght@400;700&family=Open+Sans:wght@400;700&display=swap" rel="stylesheet">
<style>
  :root {
    --stage: #8a8a8a;
    --card: #252223;
    --orange: #f55a23;
    --orange-soft: #ff8a55;
    --white: #ffffff;
    --text: #f2f2f2;
  }
  * { margin: 0; padding: 0; box-sizing: border-box; }
  html, body { width: 1200px; height: 802px; overflow: hidden; }
  body { background: var(--stage); position: relative; }

  .card {
    position: absolute;
    top: 274px;
    width: 442px;
    height: 264px;
    background: var(--card);
    overflow: hidden;
    box-shadow: 2px 4px 8px rgba(0,0,0,.35);
  }
  .card--front { left: 136px; }
  .card--back { left: 625px; }

  /* Front */
  .front__name {
    position: absolute; left: 27px; top: 44px;
    font-family: "Roboto", sans-serif; font-weight: 700;
    color: var(--white); font-size: 19px; letter-spacing: 2.5px;
    text-transform: uppercase; line-height: 1.25;
  }
  .front__phone {
    position: absolute; left: 26px; top: 127px;
    font-family: "Oswald", sans-serif; font-weight: 400;
    color: var(--orange); font-size: 29px; letter-spacing: 1px;
  }
  .front__tagline {
    position: absolute; left: 27px; top: 184px;
    font-family: "Roboto", sans-serif; color: var(--text);
    font-size: 17px; line-height: 23px;
  }
  .front__artwork { position: absolute; right: 0; top: 0; width: 230px; height: 264px; }
  .front__base {
    position: absolute; left: 0; bottom: 0; width: 100%; height: 10px;
    background: var(--white);
  }

  /* Back */
  .back__band {
    position: absolute; left: 0; top: 0; width: 66px; height: 100%;
    background: var(--orange);
  }
  .back__email {
    position: absolute; left: 33px; top: 132px;
    transform: translate(-50%, -50%) rotate(-90deg);
    white-space: nowrap;
    font-family: "Open Sans", sans-serif; font-size: 13px;
    color: var(--white);
    display: flex; align-items: center; gap: 8px;
  }
  .back__email .dot { width: 8px; height: 8px; border-radius: 50%; background: var(--white); }
  .back__brand {
    position: absolute; left: 120px; top: 82px; width: 240px;
    display: flex; align-items: center; justify-content: center; gap: 8px;
  }
  .back__brand .mark { width: 9px; height: 9px; border-radius: 50%; background: var(--orange); }
  .back__brand-name {
    font-family: "Open Sans", sans-serif; font-weight: 700;
    font-size: 16px; letter-spacing: 1.5px; color: var(--white);
    text-transform: uppercase; text-align: center; line-height: 1.2;
  }
  .services {
    position: absolute; top: 142px; list-style: none;
    font-family: "Open Sans", sans-serif; font-size: 13.5px;
    line-height: 15.8px; color: var(--text);
  }
  .services--left { left: 120px; }
  .services--right { left: 286px; }
</style>
</head>
<body>
  <section class="card card--front">
    <div class="front__name">Quillmoreton<br>Carpentry</div>
    <div class="front__phone">0455203876</div>
    <p class="front__tagline">Anything Carpentry<br>Anywhere in Sydney</p>
    <svg class="front__artwork" viewBox="0 0 230 264" role="img" aria-label="Large saw blade illustration with a city harbour skyline">
      <defs>
        <radialGradient id="bladeTone" cx="1" cy="0.75" r="1">
          <stop offset="0" stop-color="var(--orange)"/>
          <stop offset="0.7" stop-color="var(--orange)"/>
          <stop offset="1" stop-color="var(--orange-soft)"/>
        </radialGradient>
      </defs>
      <path d="M230 10 A220 220 0 0 0 10 254 L230 254 Z" fill="url(#bladeTone)"/>
    </svg>
    <div class="front__base"></div>
  </section>

  <section class="card card--back">
    <div class="back__band">
      <div class="back__email"><span class="dot"></span>quillmoretoncarpentry@mailbox.com<span class="dot"></span></div>
    </div>
    <div class="back__brand">
      <span class="mark"></span>
      <span class="back__brand-name">Quillmoreton Carpentry</span>
    </div>
    <ul class="services services--left">
      <li>Decks and Pergolas</li>
      <li>Wall and Roof Framing</li>
      <li>Doors And Windows</li>
      <li>Attic Conversions</li>
      <li>Timber Flooring</li>
      <li>Extensions</li>
    </ul>
    <ul class="services services--right">
      <li>Shop Fitats</li>
      <li>Refurbishments</li>
      <li>Fences/Gates</li>
      <li>Privacy Screens</li>
      <li>Wall Cladding</li>
      <li>&amp; more</li>
    </ul>
  </section>
</body>
</html>
```